Real Estate Development Sign

I am trying to get some good graphic design help for a new real estate development project. We need two designs for two separate large billboard-type directionals, also For Sale Signs, and also bandit directional signs. I have a company who have already given it a shot, but I don't like what they have come up with. I need it to have a WOW factor and pop to catch people's eye, but also simple and easy to read. I've attached what they have done so far. I have proofs of what has already been created and I've attached them. I've also attached the logo for the project, but I'm fine with changing the color for the logo to help make the overall signs more cohesive. I want clean, easy to read and eye catching. I will need to be able to pass the designs on to a company to have them printed for the billboards. One of them is 10x12 and the other is 8x10. Time is of the essence - I've spent too much time trying to get this other company to do what I want.
Updates

Project Deadline Extended
Reason: Need more submissions.

I would like to shoot for Black, Red, White and a touch of Yellow for the colors of the signs.

Industry/Entity Type

Graphic Design

```html
<!DOCTYPE html>
<html lang="en">
<head>
<meta charset="utf-8">
<title>The Grove at Meadow Ridge – Sign Set</title>
<link href="https://fonts.googleapis.com/css2?family=Roboto+Condensed:ital,wght@0,700;1,700&display=swap" rel="stylesheet">
<style>
  :root{
    --red:#e31e24;
    --black:#111111;
    --yellow:#ffe600;
    --white:#ffffff;
    --page:#ffffff;
    --font:"Roboto Condensed", "Arial Narrow", sans-serif;
  }
  *{box-sizing:border-box;margin:0;padding:0}
  html,body{width:1200px;height:1073px;overflow:hidden;background:var(--page)}
  body{position:relative;font-family:var(--font);font-weight:700}

  .sign{position:absolute;background:var(--red);border:2px solid var(--black);overflow:hidden}
  .frame{position:absolute;border:3px solid var(--black);box-shadow:inset 0 0 0 2px var(--yellow)}
  .line{position:absolute;left:0;right:0;top:var(--y);text-align:center;line-height:1;white-space:nowrap}
  .white{color:var(--white)}
  .ink{color:var(--black)}
  .spaced{letter-spacing:.3em;padding-left:.3em}
  .shadowed{text-shadow:2px 2px 0 var(--black)}

  .project-name{position:absolute;left:0;right:0;top:var(--y);text-align:center;color:var(--black);line-height:1}
  .project-name .main{display:block}
  .project-name .sub{display:block;letter-spacing:.02em}

  .strip{position:absolute;left:0;right:0;background:var(--yellow)}
  .band{position:absolute;left:0;right:0;bottom:0;background:var(--black)}
  .icon{position:absolute}

  /* Bandit directionals */
  .sign--openhouse{width:284px;height:214px;top:234px}
  .sign--openhouse-right{left:28px}
  .sign--openhouse-left{left:333px}
  .sign--openhouse .frame{inset:7px}
  .sign--openhouse .project-name .main{font-size:30px}
  .sign--openhouse .project-name .sub{font-size:11px}
  .sign--openhouse .headline{font-size:40px}
  .sign--openhouse .builder{font-size:12px}

  /* For sale */
  .sign--forsale{width:212px;height:283px;left:647px;top:166px}
  .sign--forsale .frame{inset:7px 7px 82px 7px}
  .sign--forsale .headline{font-size:54px}
  .sign--forsale .builder{font-size:15px}
  .sign--forsale .strip{top:201px;height:26px}
  .sign--forsale .agent{font-size:16px;top:206px}
  .sign--forsale .band{height:52px}
  .sign--forsale .phone{font-size:30px}

  /* Tall directional */
  .sign--tall{width:284px;height:422px;left:889px;top:27px}
  .sign--tall .frame{inset:8px 8px 118px 8px}
  .sign--tall .project-name .main{font-size:30px}
  .sign--tall .project-name .sub{font-size:11px}
  .sign--tall .headline{font-size:36px}
  .sign--tall .builder{font-size:13px}
  .sign--tall .price{font-size:20px}
  .sign--tall .strip{top:302px;height:14px}
  .sign--tall .band{height:106px}
  .sign--tall .now{font-size:32px}
  .sign--tall .phone{font-size:22px}

  /* 10x12 billboard */
  .sign--billboard-large{width:681px;height:566px;left:23px;top:472px}
  .sign--billboard-large .frame{inset:24px 24px 90px 24px}
  .sign--billboard-large .project-name .main{font-size:76px}
  .sign--billboard-large .project-name .sub{font-size:24px}
  .sign--billboard-large .headline{font-size:56px}
  .sign--billboard-large .builder{font-size:28px}
  .sign--billboard-large .price{font-size:40px;font-style:italic}
  .sign--billboard-large .strip{top:470px;height:14px}
  .sign--billboard-large .band{height:82px;display:flex;align-items:center;justify-content:center;gap:46px}
  .sign--billboard-large .band span{font-size:44px;color:var(--white)}

  /* 8x10 billboard */
  .sign--billboard-medium{width:452px;height:566px;left:725px;top:472px}
  .sign--billboard-medium .frame{inset:20px 20px 172px 20px}
  .sign--billboard-medium .project-name .main{font-size:56px}
  .sign--billboard-medium .project-name .sub{font-size:19px}
  .sign--billboard-medium .headline{font-size:38px}
  .sign--billboard-medium .builder{font-size:21px}
  .sign--billboard-medium .price{font-size:34px}
  .sign--billboard-medium .strip{top:382px;height:18px}
  .sign--billboard-medium .band{height:166px}
  .sign--billboard-medium .now{font-size:54px}
  .sign--billboard-medium .phone{font-size:36px}
</style>
</head>
<body>

<!-- Open house, arrow right -->
<section class="sign sign--openhouse sign--openhouse-right">
  <div class="frame"></div>
  <div class="project-name" style="--y:14px"><span class="main">The Grove</span><span class="sub">AT MEADOW RIDGE</span></div>
  <div class="line white headline shadowed" style="--y:92px">OPEN HOUSE</div>
  <svg class="icon" style="left:52px;top:146px" width="180" height="24" viewBox="0 0 180 24"><path d="M0 8h150V0l30 12-30 12v-8H0z" fill="#fff"/></svg>
  <div class="line white builder spaced" style="--y:182px">by HARLOW HOMES</div>
</section>

<!-- Open house, arrow left -->
<section class="sign sign--openhouse sign--openhouse-left">
  <div class="frame"></div>
  <div class="project-name" style="--y:14px"><span class="main">The Grove</span><span class="sub">AT MEADOW RIDGE</span></div>
  <div class="line white headline shadowed" style="--y:92px">OPEN HOUSE</div>
  <svg class="icon" style="left:52px;top:146px" width="180" height="24" viewBox="0 0 180 24"><path d="M180 8H30V0L0 12l30 12v-8h150z" fill="#fff"/></svg>
  <div class="line white builder spaced" style="--y:182px">by HARLOW HOMES</div>
</section>

<!-- For sale -->
<section class="sign sign--forsale">
  <div class="frame"></div>
  <div class="line white headline shadowed" style="--y:16px">FOR</div>
  <div class="line white headline shadowed" style="--y:68px">SALE</div>
  <div class="line white builder spaced" style="--y:128px">by</div>
  <div class="line white builder spaced" style="--y:146px">HARLOW</div>
  <div class="line white builder spaced" style="--y:164px">HOMES</div>
  <div class="strip"></div>
  <div class="line ink agent">Dana Whitfield</div>
  <div class="band"><div class="line white phone" style="--y:10px">512-555-0148</div></div>
</section>

<!-- Tall directional -->
<section class="sign sign--tall">
  <div class="frame"></div>
  <div class="project-name" style="--y:18px"><span class="main">The Grove</span><span class="sub">AT MEADOW RIDGE</span></div>
  <div class="line white headline shadowed" style="--y:98px">Custom</div>
  <div class="line white headline shadowed" style="--y:138px">Garden Homes</div>
  <div class="line white builder spaced" style="--y:182px">by HARLOW HOMES</div>
  <svg class="icon" style="left:38px;top:212px" width="20" height="70" viewBox="0 0 20 70"><path d="M10 0l10 22h-6v48H6V22H0z" fill="#fff"/></svg>
  <svg class="icon" style="left:226px;top:212px" width="20" height="70" viewBox="0 0 20 70"><path d="M10 0l10 22h-6v48H6V22H0z" fill="#fff"/></svg>
  <div class="line ink price" style="--y:234px">FROM THE LOW</div>
  <div class="line ink price" style="--y:262px">$200's</div>
  <div class="strip"></div>
  <div class="band">
    <div class="line white now" style="--y:18px">NOW SELLING</div>
    <div class="line white phone" style="--y:62px">512-555-0148</div>
  </div>
</section>

<!-- Large billboard -->
<section class="sign sign--billboard-large">
  <div class="frame"></div>
  <div class="project-name" style="--y:54px"><span class="main">The Grove</span><span class="sub">AT MEADOW RIDGE</span></div>
  <div class="line white headline shadowed" style="--y:222px">Custom Garden Homes</div>
  <div class="line white builder spaced" style="--y:292px">by HARLOW HOMES</div>
  <svg class="icon" style="left:110px;top:346px" width="460" height="54" viewBox="0 0 460 54"><path d="M0 17h400V0l60 27-60 27V37H0z" fill="#fff"/></svg>
  <div class="line ink price" style="--y:420px">FROM THE LOW $200's</div>
  <div class="strip"></div>
  <div class="band"><span>NOW SELLING</span><span>512-555-0148</span></div>
</section>

<!-- Medium billboard -->
<section class="sign sign--billboard-medium">
  <div class="frame"></div>
  <div class="project-name" style="--y:50px"><span class="main">The Grove</span><span class="sub">AT MEADOW RIDGE</span></div>
  <div class="line white headline shadowed" style="--y:164px">Custom Garden Homes</div>
  <div class="line white builder spaced" style="--y:212px">by HARLOW HOMES</div>
  <svg class="icon" style="left:44px;top:278px" width="24" height="74" viewBox="0 0 24 74"><path d="M12 0l12 24h-7v50H7V24H0z" fill="#fff"/></svg>
  <svg class="icon" style="left:384px;top:278px" width="24" height="74" viewBox="0 0 24 74"><path d="M12 0l12 24h-7v50H7V24H0z" fill="#fff"/></svg>
  <div class="line ink price" style="--y:280px">FROM THE LOW</div>
  <div class="line ink price" style="--y:324px">$200's</div>
  <div class="strip"></div>
  <div class="band">
    <div class="line white now" style="--y:30px">NOW SELLING</div>
    <div class="line white phone" style="--y:104px">512-555-0148</div>
  </div>
</section>

</body>
</html>
```